creative design for packing box of 3D paper puzzle

We want to get a packaging box design for the 3D puzzle. The packaging is for animal puzzles, like birds, insect ,wild animal. it is for young chirdren. 5-12 years old.
The box size : 12*17*2CM, 2.5CM header. Attach is some packing design ideal and our logo.
We like more nice design. It can attract the eyes. We hope all items can be use same background, and just change the color and put different animal photo on it. Box is same design, you can check the file “box-different color” . same design, just diffirent color, photo, text..
Please send us your design in diffirent color. Also You can visit our website: www.tovelk.com. you can kow how about our product.
We attach 3 items photo. You can choose one to make the designon. Our product is DIY, education. Animal with scene
Target Market(s)
Europe,Janpan,USA
Colors
Designer to choose colors to be used in the design.
Requirements
Must have
- our Logo, some nice text or signo
Nice to have
- nice background

```html
<!DOCTYPE html>
<html lang="en">
<head>
<meta charset="utf-8">
<title>3D Paper Puzzle – Packaging Box</title>
<link href="https://fonts.googleapis.com/css2?family=Bowlby+One&family=Lilita+One&display=swap" rel="stylesheet">
<style>
  :root{
    --canvas:#ffffff;
    --pink:#f76aa9;
    --cyan:#3fe3f2;
    --blue:#1fa6e0;
    --yellow:#fdd25a;
    --banner:#d9173a;
    --ring:#1830d8;
    --badge-text:#1aa3e8;
    --label-bg:#1d3fd6;
    --label-text:#ffe23a;
    --dieline:#e0252d;
    --white:#ffffff;
  }
  html,body{margin:0;padding:0;width:1200px;height:1200px;overflow:hidden;background:var(--canvas);}
  .box-art{display:block;width:1200px;height:1200px;}
  .banner{fill:var(--banner);}
  .banner-text{font-family:"Bowlby One",sans-serif;fill:var(--white);font-size:42px;}
  .banner-text--small{font-size:36px;}
  .banner-text--vertical{font-size:38px;}
  .brand{font-family:"Lilita One",sans-serif;fill:var(--label-bg);letter-spacing:2px;}
  .badge-ring{fill:var(--white);}
  .logo-spot{fill:var(--blue);}
  .age-text{font-family:"Lilita One",sans-serif;fill:var(--badge-text);font-size:36px;}
  .label-bg{fill:var(--label-bg);}
  .label-text{font-family:"Bowlby One",sans-serif;fill:var(--label-text);font-size:15px;}
  .dieline{fill:none;stroke:var(--dieline);stroke-width:1;}
</style>
</head>
<body>
<svg class="box-art" viewBox="0 0 1200 1200" xmlns="http://www.w3.org/2000/svg">
  <defs>
    <linearGradient id="puzzleBase" x1="0" y1="0" x2="1" y2="1">
      <stop offset="0" stop-color="#3fdff0"/>
      <stop offset="0.5" stop-color="#28b3e6"/>
      <stop offset="1" stop-color="#3fdff0"/>
    </linearGradient>
    <radialGradient id="pinkGlow" cx="0.5" cy="0.5" r="0.5">
      <stop offset="0" stop-color="#f76aa9" stop-opacity="0.95"/>
      <stop offset="1" stop-color="#f76aa9" stop-opacity="0"/>
    </radialGradient>
    <radialGradient id="yellowGlow" cx="0.5" cy="0.5" r="0.5">
      <stop offset="0" stop-color="#fdd25a" stop-opacity="0.95"/>
      <stop offset="1" stop-color="#fdd25a" stop-opacity="0"/>
    </radialGradient>
    <radialGradient id="blueGlow" cx="0.5" cy="0.5" r="0.5">
      <stop offset="0" stop-color="#0d8fd6" stop-opacity="0.85"/>
      <stop offset="1" stop-color="#0d8fd6" stop-opacity="0"/>
    </radialGradient>
    <linearGradient id="photoTone" x1="0" y1="0" x2="0" y2="1">
      <stop offset="0" stop-color="#f7f7f4"/>
      <stop offset="0.35" stop-color="#dfe9c8"/>
      <stop offset="0.6" stop-color="#e9e2cf"/>
      <stop offset="0.8" stop-color="#4a5247"/>
      <stop offset="1" stop-color="#2f5a3c"/>
    </linearGradient>
    <clipPath id="frontClip"><rect x="25" y="165" width="635" height="960"/></clipPath>
    <clipPath id="backClip"><rect x="660" y="80" width="490" height="917"/></clipPath>
    <filter id="textShadow" x="-5%" y="-20%" width="110%" height="140%">
      <feDropShadow dx="3" dy="3" stdDeviation="0" flood-color="#4a000c" flood-opacity="0.85"/>
    </filter>
  </defs>

  <!-- Front panel -->
  <g class="panel panel--front">
    <g clip-path="url(#frontClip)" role="img" aria-label="Colourful jigsaw-piece background pattern in pink, cyan, blue and yellow">
      <rect x="25" y="165" width="635" height="960" fill="url(#puzzleBase)"/>
      <circle cx="80" cy="230" r="170" fill="url(#pinkGlow)"/>
      <circle cx="380" cy="200" r="160" fill="url(#pinkGlow)"/>
      <circle cx="620" cy="470" r="150" fill="url(#yellowGlow)"/>
      <circle cx="60" cy="620" r="160" fill="url(#yellowGlow)"/>
      <circle cx="560" cy="760" r="170" fill="url(#pinkGlow)"/>
      <circle cx="300" cy="460" r="150" fill="url(#blueGlow)"/>
      <circle cx="90" cy="1060" r="170" fill="url(#pinkGlow)"/>
      <circle cx="420" cy="1000" r="150" fill="url(#yellowGlow)"/>
      <circle cx="620" cy="1100" r="120" fill="url(#blueGlow)"/>
    </g>
    <path class="dieline" d="M110 180 H580 M110 180 V1115 M580 180 V1115 M35 240 H650 M35 1060 H650 M110 1115 H580 M35 240 V1060 M650 240 V1060"/>

    <rect class="banner" x="110" y="258" width="470" height="48"/>
    <text class="banner-text banner-text--small" x="126" y="298" textLength="364" lengthAdjust="spacingAndGlyphs" filter="url(#textShadow)">3D PAPER PUZZLE</text>
    <circle class="badge-ring" cx="535" cy="281" r="30" stroke="var(--pink)" stroke-width="5"/>
    <text class="brand" x="535" y="286" font-size="12" text-anchor="middle">TOVELK</text>

    <rect class="banner" x="110" y="340" width="470" height="56"/>
    <text class="banner-text" x="122" y="388" textLength="448" lengthAdjust="spacingAndGlyphs" filter="url(#textShadow)">3D PAPER PUZZLE</text>

    <circle class="logo-spot" cx="508" cy="458" r="34"/>
    <text class="brand" x="508" y="520" font-size="26" text-anchor="middle">TOVELK</text>

    <rect class="banner" x="45" y="410" width="60" height="480"/>
    <text class="banner-text banner-text--vertical" transform="translate(92 870) rotate(-90)" textLength="440" lengthAdjust="spacingAndGlyphs" filter="url(#textShadow)">3D PAPER PUZZLE</text>
    <rect class="banner" x="596" y="410" width="50" height="475"/>
    <text class="banner-text banner-text--vertical" transform="translate(604 425) rotate(90)" textLength="445" lengthAdjust="spacingAndGlyphs" filter="url(#textShadow)">3D PAPER PUZZLE</text>

    <circle class="badge-ring" cx="70" cy="362" r="30" stroke="var(--pink)" stroke-width="5"/>
    <text class="brand" x="70" y="366" font-size="11" text-anchor="middle">TOVELK</text>
    <circle class="badge-ring" cx="620" cy="362" r="30" stroke="var(--ring)" stroke-width="5"/>
    <text class="brand" x="620" y="366" font-size="11" text-anchor="middle">TOVELK</text>
    <circle class="badge-ring" cx="70" cy="932" r="30" stroke="var(--ring)" stroke-width="5"/>
    <text class="brand" x="70" y="936" font-size="11" text-anchor="middle">TOVELK</text>
    <circle class="badge-ring" cx="620" cy="932" r="30" stroke="var(--pink)" stroke-width="5"/>
    <text class="brand" x="620" y="936" font-size="11" text-anchor="middle">TOVELK</text>

    <circle cx="345" cy="702" r="213" fill="url(#photoTone)" stroke="var(--ring)" stroke-width="8" role="img" aria-label="Photo of the assembled paper panda puzzle with bamboo and a tree stump on a green base"/>
    <rect class="label-bg" x="367" y="557" width="138" height="24"/>
    <text class="label-text" x="436" y="575" text-anchor="middle">PANDA PUZZLE</text>

    <circle class="badge-ring" cx="237" cy="895" r="70" stroke="var(--ring)" stroke-width="6"/>
    <text class="age-text" x="237" y="877" text-anchor="middle">5 TO 12</text>
    <text class="age-text" x="237" y="909" text-anchor="middle">YEARS</text>
    <text class="age-text" x="237" y="941" text-anchor="middle">OLD</text>

    <rect class="banner" x="110" y="995" width="470" height="56"/>
    <text class="banner-text" transform="translate(568 1006) rotate(180)" textLength="446" lengthAdjust="spacingAndGlyphs" filter="url(#textShadow)">3D PAPER PUZZLE</text>
  </g>

  <!-- Back panel with hang header -->
  <g class="panel panel--back">
    <g clip-path="url(#backClip)" role="img" aria-label="Colourful jigsaw-piece background pattern in pink, cyan, blue and yellow">
      <rect x="660" y="80" width="490" height="917" fill="url(#puzzleBase)"/>
      <circle cx="760" cy="120" r="150" fill="url(#pinkGlow)"/>
      <circle cx="1100" cy="170" r="150" fill="url(#yellowGlow)"/>
      <circle cx="700" cy="300" r="130" fill="url(#yellowGlow)"/>
      <circle cx="1000" cy="290" r="140" fill="url(#pinkGlow)"/>
      <circle cx="690" cy="700" r="150" fill="url(#yellowGlow)"/>
      <circle cx="1130" cy="560" r="150" fill="url(#pinkGlow)"/>
      <circle cx="900" cy="950" r="150" fill="url(#yellowGlow)"/>
      <circle cx="700" cy="960" r="120" fill="url(#pinkGlow)"/>
      <circle cx="1130" cy="900" r="130" fill="url(#blueGlow)"/>
    </g>
    <path class="dieline" d="M660 220 H1150 M660 320 H1185 V985 H1150 M660 997 H1150"/>
    <rect class="dieline" x="835" y="160" width="120" height="32" rx="16"/>
    <rect class="dieline" x="835" y="250" width="120" height="30" rx="15"/>

    <rect class="banner" x="660" y="340" width="485" height="54"/>
    <text class="banner-text" x="670" y="386" textLength="448" lengthAdjust="spacingAndGlyphs" filter="url(#textShadow)">3D PAPER PUZZLE</text>

    <circle cx="900" cy="640" r="213" fill="url(#photoTone)" stroke="var(--ring)" stroke-width="8" role="img" aria-label="Photo of the assembled paper panda puzzle with bamboo and a tree stump on a green base"/>
    <rect class="label-bg" x="920" y="490" width="138" height="25"/>
    <text class="label-text" x="989" y="509" text-anchor="middle">PANDA PUZZLE</text>

    <circle class="badge-ring" cx="790" cy="830" r="70" stroke="var(--ring)" stroke-width="6"/>
    <text class="age-text" x="790" y="812" text-anchor="middle">5 TO 12</text>
    <text class="age-text" x="790" y="844" text-anchor="middle">YEARS</text>
    <text class="age-text" x="790" y="876" text-anchor="middle">OLD</text>

    <circle class="badge-ring" cx="1031" cy="880" r="68" stroke="var(--ring)" stroke-width="6"/>
    <circle class="logo-spot" cx="1031" cy="858" r="24"/>
    <text class="brand" x="1031" y="922" font-size="24" text-anchor="middle">TOVELK</text>
  </g>
</svg>
</body>
</html>
```